Pelvin Advisory Business Card Design

Business card for business consulting company, using attached logo. We do financial and strategic consulting, and want a clean, professional image with a bit of fun. Our logo is a flat whale tail, which symbolizes the Orca whale, a highly collaborative, group based animal that is very successful in navigating the ocean, protecting the herd, and hunting. We like the logo that is blue and gray on white one one side, but would be open to a blue card with white lettering on the other side... or whatever you'd suggest
Updates
Hi all - I have had the logo modified to take the shadowing off the tail. I will post it on the brief... under a file name called updated logo. thank you Added Saturday, April 25, 2015
Target Market(s)
Small to medium sized businesses ($10M to $500M in revenue per year), financial and sales executives, general managers, attorneys and CPAs
Industry/Entity Type
Financial
Contact Information for Business Card
Want company name, contact info - name, title, telephone, email, website, linkedin, twitter and Facebook. No physical address yet.
Requirements
Must have
- contemporary design, bold, strong, confident but with a bit of fun. prominently feature the logo and the whale tail icon
Nice to have
- unique touches that would differentiate us from a regular card... for example, logo and writing all on front on white background, but on back - logo in white on a blue background
- open to idea of different shapes of card than standard... but not sure

```html
<!DOCTYPE html>
<html lang="en">
<head>
<meta charset="utf-8">
<title>Pelvin Advisory Business Card</title>
<link rel="stylesheet" href="https://fonts.googleapis.com/css2?family=Open+Sans:wght@400;600;700&display=swap">
<style>
  :root {
    --navy: #1f3f73;
    --navy-deep: #17315c;
    --navy-soft: #2a4d86;
    --grey-text: #6b6b6b;
    --grey-light: #a9a9a9;
    --paper: #ffffff;
    --backdrop: #e9ebee;
    --social: #2b7bbf;
  }
  * { box-sizing: border-box; margin: 0; padding: 0; }
  html, body {
    width: 1200px; height: 900px; overflow: hidden;
    background: var(--backdrop);
    font-family: "Open Sans", Arial, sans-serif;
  }
  .canvas { position: relative; width: 1200px; height: 900px; }
  .card {
    position: absolute; left: 320px; width: 560px; height: 320px;
    border-radius: 4px; overflow: hidden;
    box-shadow: 0 6px 18px rgba(0,0,0,0.18);
  }
  /* back side */
  .card-back {
    top: 90px;
    background: linear-gradient(135deg, var(--navy-soft) 0%, var(--navy) 45%, var(--navy-deep) 100%);
  }
  .back-mark {
    position: absolute; left: 70px; top: 60px; width: 200px; height: 200px;
    border-radius: 26px; background: rgba(255,255,255,0.05);
  }
  .back-brand {
    position: absolute; right: 40px; bottom: 92px; text-align: right; color: var(--paper);
  }
  .back-brand .brand-name { font-size: 38px; font-weight: 600; letter-spacing: -1px; line-height: 1; }
  .back-brand .brand-tag { font-size: 12px; font-weight: 400; margin-top: 3px; }
  /* front side */
  .card-front { top: 490px; background: var(--paper); }
  .front-brand { position: absolute; left: 60px; top: 48px; width: 440px; }
  .front-brand .brand-square {
    position: absolute; left: 0; top: 4px; width: 58px; height: 58px;
    border-radius: 9px; background: var(--navy);
  }
  .front-brand .brand-name {
    position: absolute; left: 72px; top: 0; font-size: 46px; font-weight: 600;
    letter-spacing: -1.5px; line-height: 66px; color: var(--navy); white-space: nowrap;
  }
  .front-brand .brand-tag {
    position: absolute; right: 0; top: 66px; font-size: 14px; color: var(--navy);
  }
  .person { position: absolute; right: 300px; top: 178px; text-align: right; }
  .person .name { font-size: 24px; font-weight: 700; color: var(--navy); line-height: 1.2; }
  .person .title { font-size: 14px; color: var(--grey-text); }
  .divider { position: absolute; left: 278px; top: 168px; width: 1px; height: 104px; background: #d4d4d4; }
  .contact { position: absolute; left: 296px; top: 170px; list-style: none; }
  .contact li {
    display: flex; align-items: center; gap: 8px;
    font-size: 16px; color: var(--grey-text); height: 25px;
  }
  .contact svg { width: 14px; height: 14px; fill: var(--navy); flex: none; }
  .social { display: flex; gap: 4px; margin-top: 4px; }
  .social span { width: 18px; height: 18px; background: var(--social); border-radius: 2px; }
</style>
</head>
<body>
<div class="canvas">
  <section class="card card-back" aria-label="Card back">
    <div class="back-mark"></div>
    <div class="back-brand">
      <div class="brand-name">Pelvin Advisory</div>
      <div class="brand-tag">business consulting</div>
    </div>
  </section>

  <section class="card card-front" aria-label="Card front">
    <div class="front-brand">
      <div class="brand-square"></div>
      <div class="brand-name">Pelvin Advisory</div>
      <div class="brand-tag">business consulting</div>
    </div>
    <div class="person">
      <div class="name">Daniel Whitford</div>
      <div class="title">Managing Member</div>
    </div>
    <div class="divider"></div>
    <ul class="contact">
      <li><svg viewBox="0 0 14 14"><path d="M4 0h6a1 1 0 0 1 1 1v12a1 1 0 0 1-1 1H4a1 1 0 0 1-1-1V1a1 1 0 0 1 1-1zm0 2v9h6V2z"/></svg>(555) 014-2290</li>
      <li><svg viewBox="0 0 14 14"><path d="M0 3h14v8H0zm1 1v.4l6 3.6 6-3.6V4z"/></svg>daniel@pelvinadvisory.com</li>
      <li><svg viewBox="0 0 14 14"><path d="M7 0a7 7 0 1 0 0 14A7 7 0 0 0 7 0zm0 1.5c.8 0 1.7 1.6 2 4H5c.3-2.4 1.2-4 2-4zM1.6 6.5h2.4c0 .4 0 .7 0 1H1.6zM5 8.5h4c-.3 2.4-1.2 4-2 4s-1.7-1.6-2-4zm5-2h2.4v1H10z"/></svg>www.pelvinadvisory.com</li>
      <li class="social"><span></span><span></span><span></span></li>
    </ul>
  </section>
</div>
</body>
</html>
```